Book Cover (HALF OF ALL WORRIES FADE AWAY)

This book is a series of blog posts from my blog, Notes Fit for Borrowing, which is at glenmarwick.com/blog.
The book is to be called:
HALF OF ALL WORRIES FADE AWAY
And 51 other Notes Fit for Borrowing from the Small Business Sage
(Notes Fit for Borrowing) should be italicized.
My name is Glen Marwick, M.B.A.

I will need three variations for my paperback, hardcover and e-book.
Here are some of the blog titles and their topics:
Preparing Your Small Business For Recession small business recession
Should I Incorporate My Business? Should I Incorporate My Business?
Alternative to Minority Shareholder In Small Private Companies minority shareholder
Small Business Culture – Getting it Right Small Business Culture
What is The Right Way to Fire Someone The Right Way to Fire Someone
The Five Basic Leadership Principles Leadership Principles
10 Tips for New Entrepreneurs – Sure Ways to Increase Your Chances of Success
10 things to consider before becoming an entrepreneur
Strategy vs Biz Plans small business strategy
Closing Sales close the sale
Breakeven break even
Growth makes cash flow suck cash flow issues
Think Twice About Offering Early Payment Discounts prepayment discounts
Firing Customers firing customers
Collections best practices getting paid faster
The Cash Flow Statement cash flow statement
Using Paralegals paralegal
Radical Candor radical candor
Why No is the Second Best Word to a Salesperson's ears value of no
The $8 Million Problem -
Contractor vs Employee contractor vs employee
The Vantrell sales tactic
Systems Turn Goals From Dreams Into Reality Systems vs Goals
The Importance of Realistic Goals stretch goals
Why The Owner Must Review Every Hire hiring for values
Systems Thinking for Small Biz: The Case for SOPs systems thinking
Trust Your Gut business intuition
Grease and friction grease vs friction
Left alone, 90% of problems solve themselves strategic inaction
Referrals Are Great—But Not a Growth Strategy referrals
The Lean Marketing Machine: 7 Hacks to Grow Your Small Business Fast marketing hacks
The Small Business Health Check small business health check
How to Spot a Customer Headed for Trouble — Before They Take You Down With Them customer warning signs
We Are What We Repeatedly Do habits
The Smartest People Know When to Play Dumb playing dumb
Before You Scale, Do the Math unit economics
AI for Small Business: Practical Tools and Use Cases AI for Small Business
Title: Tell Me Right Now—Why Can’t We Raise Your Prices? small business pricing
Why Your Real Competitor Isn’t Who You Think creative destruction
Good Enough Might Be Great satisficing
Bootstrapping: Building Your Business on Your Terms bootstrapping
Building Resilient Companies That Never Have to Bet the Farm bet the farm
We Always Overshoot: From Fiber to Cannabis to AI AI overbuild
A Bias Toward Action bias toward ation
Choosing the Right Business Owner Title business owner title
Jobs to Be Done: Understanding What Your Customers Really Want Jobs to Be Done
Forget Money. Here’s What Really Motivates People. motivation

Target Market(s)

Small business operators, business school students

Industry/Entity Type

Small business

Colors

Designer to choose colors to be used in the design.

Requirements
Should not have
• Should not look cartoonish

```html
<!DOCTYPE html>
<html lang="en">
<head>
<meta charset="UTF-8">
<title>Half of All Worries Fade Away — Book Cover</title>
<link rel="stylesheet" href="https://fonts.googleapis.com/css2?family=DM+Serif+Display&family=Libre+Baskerville:ital,wght@0,400;1,400&display=swap">
<style>
  :root {
    --backdrop: #e6e4e0;
    --cover-navy: #0e1626;
    --cover-deep: #0a111e;
    --art-teal: #2f6f80;
    --art-blue: #173049;
    --glow-amber: #f2b64a;
    --title-white: #f4f1ea;
    --title-gold: #e9c85e;
    --rule: #8b8f99;
  }
  html, body {
    margin: 0;
    padding: 0;
    width: 1200px;
    height: 875px;
    overflow: hidden;
    background: var(--backdrop);
  }
  .canvas {
    width: 1200px;
    height: 875px;
    display: flex;
    align-items: center;
    justify-content: center;
  }
  .book-cover {
    position: relative;
    width: 600px;
    height: 815px;
    background: linear-gradient(180deg, var(--cover-navy) 0%, var(--cover-deep) 100%);
    box-shadow: 0 14px 36px rgba(0, 0, 0, 0.28);
    overflow: hidden;
    display: flex;
    flex-direction: column;
  }
  .cover-art {
    height: 430px;
    background:
      radial-gradient(circle at 40% 26%, rgba(242, 182, 74, 0.95) 0%, rgba(242, 182, 74, 0.45) 9%, rgba(242, 182, 74, 0) 24%),
      linear-gradient(180deg, var(--art-blue) 0%, #1d4a5e 55%, var(--art-teal) 78%, var(--cover-navy) 100%);
  }
  .cover-text {
    flex: 1;
    padding: 34px 48px 0;
    text-align: center;
  }
  .book-title {
    margin: 0;
    font-family: "DM Serif Display", Georgia, serif;
    font-weight: 400;
    font-size: 50px;
    line-height: 1.08;
    letter-spacing: 0.5px;
    color: var(--title-white);
  }
  .book-title .title-accent {
    display: block;
    color: var(--title-gold);
  }
  .book-subtitle {
    margin: 20px 0 0;
    font-family: "Libre Baskerville", Georgia, serif;
    font-size: 19px;
    line-height: 1.4;
    color: var(--title-white);
  }
  .book-subtitle em {
    color: var(--title-gold);
  }
  .title-rule {
    width: 300px;
    height: 1px;
    margin: 22px auto 22px;
    background: var(--rule);
    border: 0;
  }
  .book-author {
    margin: 0;
    font-family: "Libre Baskerville", Georgia, serif;
    font-size: 26px;
    letter-spacing: 0.5px;
    color: var(--title-white);
  }
</style>
</head>
<body>
  <main class="canvas">
    <section class="book-cover">
      <div class="cover-art" role="img" aria-label="Illustration of a glowing lightbulb above a standing silhouetted figure, with business people working at desks and small business icons around them"></div>
      <div class="cover-text">
        <h1 class="book-title">Half of All Worries <span class="title-accent">Fade Away</span></h1>
        <p class="book-subtitle">And 51 other <em>Notes Fit for Borrowing</em><br>from the Small Business Sage</p>
        <hr class="title-rule">
        <p class="book-author">Glen Marwick, M.B.A.</p>
      </div>
    </section>
  </main>
</body>
</html>
```